Webdesign for blog, vlog and website
The designs for my website were better than what I expected when I started this contest. I knew I needed a call-to-action on my homepage, but I thought it wouldn't be possible and I didn't ask for it either. But Anselmo did it anyway. Furthermore, his design looked very good. For that reason I selected him as winner already before I should. I am very happy.

```html
<!DOCTYPE html>
<html lang="en">
<head>
<meta charset="utf-8">
<title>Voriqa – Blog &amp; Vlog</title>
<link href="https://fonts.googleapis.com/css2?family=Nunito:wght@800;900&family=Open+Sans:wght@300;400;600;700&display=swap" rel="stylesheet">
<style>
:root{
  --navy:#012266;
  --orange:#ff5000;
  --page-grey:#f0f0f0;
  --white:#ffffff;
  --ink:#111111;
  --muted:#555555;
  --nav-ink:#333333;
}
*{box-sizing:border-box;margin:0;padding:0}
html,body{width:1200px;height:1116px;overflow:hidden;background:var(--white)}
body{font-family:'Open Sans',sans-serif;color:var(--ink);position:relative}
.site-header{position:absolute;left:0;top:0;width:1200px;height:86px;background:#fafafa}
.brand-name{position:absolute;left:132px;top:26px;font-family:'Open Sans',sans-serif;font-weight:700;font-size:28px;color:var(--navy);line-height:1.2}
.main-nav{position:absolute;left:628px;top:34px;display:flex;gap:18px;font-size:15.5px;font-weight:400;color:var(--nav-ink)}
.feature-band{position:absolute;left:0;top:86px;width:1200px;height:88px;background:var(--navy)}
.band-button{position:absolute;top:27px;width:192px;height:34px;background:var(--orange);border:1px solid var(--white);color:var(--white);font-size:20px;font-weight:300;text-align:center;line-height:31px}
.band-button b{font-weight:700}
.band-button.blog{left:365px}
.band-button.vlog{left:629px}
.content-area{position:absolute;left:0;top:262px;width:1200px;height:783px;background:var(--page-grey)}
.vlog-panel{position:absolute;left:60px;top:285px;width:1066px;height:740px;background:var(--white)}
.panel-title{position:absolute;left:132px;top:298px;font-family:'Nunito',sans-serif;font-weight:900;font-size:20px;color:var(--navy);letter-spacing:.5px}
.panel-title span{color:var(--orange)}
.title-play{position:absolute;left:363px;top:296px;width:56px;height:33px;background:var(--navy);border-radius:2px}
.title-play svg{position:absolute;left:19px;top:8px}
.vlog-card{position:absolute;width:313px}
.vlog-thumb{width:313px;height:195px;border-radius:3px}
.vlog-text{padding:8px 10px 0;font-size:13.5px;line-height:17.6px;color:var(--muted)}
.vlog-text strong{color:var(--ink);font-weight:700}
.vlog-views{padding:0 10px;font-size:14px;color:#777;line-height:17px}
.view-button{position:absolute;right:17px;bottom:-24px;width:97px;height:26px;background:var(--navy);border:1px solid var(--orange);border-radius:2px;color:var(--white);font-family:'Nunito',sans-serif;font-weight:900;font-size:16px;line-height:24px;padding-left:5px}
.view-button i{position:absolute;right:3px;top:3px;width:34px;height:18px;background:#0a3a8a;border:1px solid var(--white);border-radius:2px}
.view-button i svg{position:absolute;left:11px;top:3px}
.card-1{left:132px;top:337px}
.card-2{left:463px;top:337px}
.card-3{left:793px;top:337px}
.card-4{left:132px;top:670px}
.card-5{left:465px;top:670px}
.newest-tile{position:absolute;left:795px;top:672px;width:313px;height:194px;background:var(--orange);border-radius:2px;color:var(--white);font-size:21px;font-weight:300;text-align:center;line-height:194px}
.newest-tile b{font-weight:700}
.browse-strip{position:absolute;left:0;top:1045px;width:1200px;height:71px;background:var(--white);border-top:1px solid #e2e2e2}
.browse-button{position:absolute;left:485px;top:19px;width:220px;height:42px;background:var(--orange);color:#2a63c9;font-family:'Nunito',sans-serif;font-weight:800;font-size:22px;text-align:center;line-height:42px}
</style>
</head>
<body>
<header class="site-header">
  <div class="brand-name">Voriqa</div>
  <nav class="main-nav"><span>SHOP</span><span>FORUM</span><span>ABOUT</span><span>CONTACT</span></nav>
</header>

<section class="feature-band">
  <div class="band-button blog">read <b>Blog</b></div>
  <div class="band-button vlog">watch <b>Vlog</b></div>
</section>

<div class="content-area"></div>
<main class="vlog-panel"></main>

<h2 class="panel-title">Most watched <span>vlogs:</span></h2>
<div class="title-play"><svg width="20" height="18" viewBox="0 0 20 18"><polygon points="0,0 20,9 0,18" fill="#ff5000"/></svg></div>

<article class="vlog-card card-1">
  <div class="vlog-thumb" role="img" aria-label="Photo of a young woman pointing at a red play button" style="background:linear-gradient(90deg,#e9a0a0 0%,#f1e7e2 45%,#c99a78 70%,#ece8e4 100%)"></div>
  <p class="vlog-text"><strong>Regularly we see children of failed asylum</strong> seekers on TV who need to go back to their own countries. They and the people who know them well then tell us why it is so bad that...</p>
  <p class="vlog-views">160.989 Aufrufe</p>
  <div class="view-button">VIEW<i><svg width="12" height="11" viewBox="0 0 12 11"><polygon points="0,0 12,5.5 0,11" fill="#ff5000"/></svg></i></div>
</article>

<article class="vlog-card card-2">
  <div class="vlog-thumb" role="img" aria-label="Photo of a cyclist passing a historic parliament building at sunset" style="background:linear-gradient(160deg,#f5ecd8 0%,#d8b27a 45%,#8a7656 75%,#6a6a60 100%)"></div>
  <p class="vlog-text"><strong>Regularly we see children of failed asylum</strong> seekers on TV who need to go back to their own countries. They and the people who know them well then tell us why it is so bad that...</p>
  <p class="vlog-views">160.989 Aufrufe</p>
  <div class="view-button">VIEW<i><svg width="12" height="11" viewBox="0 0 12 11"><polygon points="0,0 12,5.5 0,11" fill="#ff5000"/></svg></i></div>
</article>

<article class="vlog-card card-3">
  <div class="vlog-thumb" role="img" aria-label="Photo of a professional video camera in a crowd" style="background:linear-gradient(90deg,#7a5a4a 0%,#2a2a2e 40%,#3b4f6a 70%,#b07a60 100%)"></div>
  <p class="vlog-text"><strong>Regularly we see children of failed asylum</strong> seekers on TV who need to go back to their own countries. They and the people who know them well then tell us why it is so bad that...</p>
  <p class="vlog-views">160.989 Aufrufe</p>
  <div class="view-button">VIEW<i><svg width="12" height="11" viewBox="0 0 12 11"><polygon points="0,0 12,5.5 0,11" fill="#ff5000"/></svg></i></div>
</article>

<article class="vlog-card card-4">
  <div class="vlog-thumb" role="img" aria-label="Photo of a woman in a red hat holding a nasal spray in front of a pharmacy" style="background:linear-gradient(160deg,#5e8f8a 0%,#c7a6a8 35%,#d84a4a 70%,#6a4a40 100%)"></div>
  <p class="vlog-text"><strong>Regularly we see children of failed asylum</strong> seekers on TV who need to go back to their own countries. They and the people who know them well then tell us why it is so bad that...</p>
  <p class="vlog-views">160.989 Aufrufe</p>
  <div class="view-button">VIEW<i><svg width="12" height="11" viewBox="0 0 12 11"><polygon points="0,0 12,5.5 0,11" fill="#ff5000"/></svg></i></div>
</article>

<article class="vlog-card card-5">
  <div class="vlog-thumb" role="img" aria-label="Photo of a blurred crowd at a demonstration" style="background:linear-gradient(150deg,#a08a78 0%,#6e6470 45%,#4a4258 75%,#8a6a70 100%)"></div>
  <p class="vlog-text"><strong>Regularly we see children of failed asylum</strong> seekers on TV who need to go back to their own countries. They and the people who know them well then tell us why it is so bad that...</p>
  <p class="vlog-views">160.989 Aufrufe</p>
  <div class="view-button">VIEW<i><svg width="12" height="11" viewBox="0 0 12 11"><polygon points="0,0 12,5.5 0,11" fill="#ff5000"/></svg></i></div>
</article>

<div class="newest-tile">see <b>NEWEST</b></div>

<footer class="browse-strip">
  <div class="browse-button">Browse</div>
</footer>
</body>
</html>
```